Postcard Design

I need a two-sided promotional postcard designed to address the key business areas of my gluten free wellness retreat.

Please Note: The "mailer" template is not required for the reverse as these postcards are for event handouts only. Please use the attached "front" template for each side (both front and back)

Possibly, services on one side and photos/visuals on the other side with contact information on either or both sides.

www.sunmeadowhaven.net is my website.

Key business areas:

STAY: Retreat stays + associated care program
PLAY: Bed and Breakfast
LEARN: Individual Health Coaching
GROW: Community classes / events / cooking classes

Retreat Stay Client: Female, 40+. Expendable income, but she likely has a very busy career and family so she does not have the time to spend this on herself. Her wellness takes a backseat to her career and family life. She often remembers being “thinner when she was younger” and has a lot of preconceived notions about dieting. She is open to alternative healthcare options, and thinks she does a pretty good job keeping up with them via Dr. Vane, and magazine articles etc. She needs a compassionate, non-intimidating care provider who she trusts will not “judge” her.

Coaching Client: Male + Female, from mid-40s to retirement age and older. They likely also have some amount of expendable income, and are not necessarily bound my medical or other insurance in terms of seeking alternative treatment. In their earlier adult years they were likely active and well-traveled. They have some adult children who are also quite successful, and so in their golden years, they are comfortable to spend money on themselves rather than assist adult children/grandkids. Frankly, they can somewhat skeptical of alternative wellness providers. They likely suffer from a myriad of age related maladies, and need a compassionate standard of care.

Visual Identity:

 Color/visual TO DO:
o Align color palate with warmth of the desert / desert scenery – without being to “Western”
o Incorporate sky blues, and tones found in flowers
o Feature vegetal, floral, or similar imagery (preferably that of the actual retreat location and surrounding
area)

 Color /visual DO NOT DO:
o Overly bright, pop color tones
o Sharp, bright tones
o Overtly “stock” photos – note: you can use these, but try to steer clear of obviously fake photos.

Industry/Entity Type

Healthcare

Requirements
Must have
• Must list services offers
Must use real photos of retreat and/or cooking shots
Must use at least one photo of the pool

Must have email, website and phone number

I do not want the mail ready set up. These postcards are for event handouts only.

I would like different information on each side of the postcard. Possibly, services on one side and photos/visuals on the other side with contact information on either or both sides. I attached an example of previous printed materials as well as my website to get a feel for my business.

Additionally, once this project is done, I would like to work with the designer for other elements? I'm looking for a matching business card and tri-fold brochure.

```html
<!DOCTYPE html>
<html lang="en">
<head>
<meta charset="utf-8">
<title>Sun Meadow Haven – Postcard</title>
<link rel="stylesheet" href="https://fonts.googleapis.com/css2?family=Great+Vibes&family=PT+Sans:wght@400;700&family=PT+Sans+Narrow:wght@700&family=Source+Sans+3:wght@300;400&display=swap">
<style>
  :root {
    --backdrop: #2a2a2a;
    --sage: #b8d399;
    --sage-deep: #a6c585;
    --panel: #ffffff;
    --panel-edge: #d9d9d9;
    --crimson: #c3244c;
    --leaf: #94c16f;
    --ink: #3f3f3f;
    --ink-soft: #555555;
    --night: #2b2622;
  }
  * { box-sizing: border-box; margin: 0; padding: 0; }
  html, body { width: 1200px; height: 1200px; overflow: hidden; }
  body {
    background: var(--backdrop);
    font-family: "Source Sans 3", "PT Sans", sans-serif;
    color: var(--ink);
    position: relative;
  }
  .postcard {
    position: absolute;
    background: linear-gradient(135deg, var(--sage), var(--sage-deep));
  }
  .postcard--services { left: 420px; top: 26px; width: 726px; height: 558px; }
  .postcard--visuals { left: 62px; top: 614px; width: 732px; height: 562px; }

  .panel {
    position: absolute;
    background: var(--panel);
    border: 5px solid #eeeeee;
    outline: 1px solid var(--panel-edge);
  }
  .photo { position: absolute; border: 5px solid #eeeeee; }

  /* Services side */
  .services-panel { left: 14px; top: 20px; width: 470px; height: 380px; text-align: center; padding: 8px 24px; }
  .services-title { font-family: "Great Vibes", cursive; color: var(--crimson); font-size: 40px; font-weight: 400; line-height: 1.1; }
  .service-name { color: var(--leaf); font-size: 17px; font-weight: 300; margin-top: 6px; }
  .service-text { font-size: 13px; line-height: 1.35; color: var(--ink-soft); }
  .service-text + .service-text { margin-top: 6px; }
  .service-note { font-size: 13px; line-height: 1.35; color: var(--crimson); margin-top: 10px; }

  .bio-panel { left: 14px; top: 412px; width: 470px; height: 128px; }
  .bio-photo { left: 10px; top: 8px; width: 86px; height: 104px; position: absolute;
    background: linear-gradient(180deg, #8a8f95, #5e6166 60%, #7a7468); }
  .bio-body { position: absolute; left: 115px; top: 10px; }
  .bio-name { font-family: "PT Sans", sans-serif; color: var(--crimson); font-size: 19px; font-weight: 400; }
  .bio-list { list-style: none; font-size: 16px; color: var(--ink-soft); line-height: 1.3; }
  .bio-list li::before { content: "• "; color: var(--crimson); }

  .contact-column { left: 492px; top: 20px; width: 220px; height: 520px; position: absolute; border: 5px solid #eeeeee; }
  .sunset-photo { position: absolute; left: 0; top: 0; width: 100%; height: 380px;
    background: linear-gradient(160deg, #6a5a52 0%, #c98a3e 35%, #f4b950 50%, #a5622a 70%, #3d2a1e 100%); }
  .brand-strip { position: absolute; left: 0; top: 380px; width: 100%; height: 52px; background: var(--panel);
    display: flex; align-items: center; justify-content: center; gap: 8px; }
  .brand-name { font-family: "PT Sans", sans-serif; font-size: 12px; letter-spacing: 1.5px; color: var(--ink); text-transform: uppercase; }
  .brand-dot { width: 14px; height: 14px; border-radius: 50%; background: var(--crimson); }
  .contact-block { position: absolute; left: 0; top: 432px; width: 100%; bottom: 0; background: var(--night);
    color: #ffffff; text-align: center; font-family: "PT Sans Narrow", sans-serif; font-weight: 700; padding-top: 6px; }
  .contact-phone { font-size: 25px; line-height: 1.1; }
  .contact-line { font-size: 14px; line-height: 1.25; }

  /* Visuals side */
  .pool-photo { left: 14px; top: 20px; width: 380px; height: 260px;
    background: linear-gradient(180deg, #d9c6ad 0%, #b08a6a 35%, #8a9a6a 55%, #4ea3b8 78%, #c7b59c 100%); }
  .offer-panel { left: 402px; top: 20px; width: 316px; height: 260px; text-align: center; padding-top: 40px; }
  .offer-title { font-family: "Source Sans 3", sans-serif; font-weight: 400; font-size: 31px; color: var(--crimson); margin-bottom: 10px; }
  .offer-list { list-style: none; font-size: 20px; font-weight: 300; color: var(--ink); line-height: 1.33; }

  .motto-band { position: absolute; left: 14px; top: 292px; width: 704px; height: 52px; background: var(--crimson);
    border: 1px dashed rgba(255,255,255,0.6); outline: 2px solid var(--crimson);
    color: #ffffff; font-size: 23px; font-weight: 300; display: flex; align-items: center; justify-content: center; }

  .identity-panel { left: 14px; top: 356px; width: 486px; height: 190px; }
  .identity-mark { position: absolute; left: 10px; top: 20px; width: 190px; height: 140px;
    display: flex; flex-direction: column; align-items: center; justify-content: center; gap: 14px; }
  .identity-dot { width: 46px; height: 46px; border-radius: 50%; background: var(--crimson); }
  .identity-name { font-family: "PT Sans", sans-serif; font-size: 13px; letter-spacing: 1.8px; text-transform: uppercase; color: var(--ink); }
  .identity-divider { position: absolute; left: 212px; top: 18px; width: 1px; height: 144px; background: #cccccc; }
  .identity-contact { position: absolute; right: 12px; top: 12px; text-align: right; }
  .identity-title { font-family: "Great Vibes", cursive; color: var(--crimson); font-size: 33px; font-weight: 400; line-height: 1.2; margin-bottom: 8px; }
  .identity-line { font-size: 17px; font-weight: 300; color: var(--ink); line-height: 1.25; }
  .identity-city { margin-top: 8px; }

  .market-photo { left: 512px; top: 356px; width: 206px; height: 190px;
    background: linear-gradient(180deg, #dfe6d8 0%, #9db38a 40%, #e9e6e2 65%, #6d8a55 100%); }
</style>
</head>
<body>

<section class="postcard postcard--services">
  <div class="panel services-panel">
    <h1 class="services-title">Classes and Services</h1>
    <h2 class="service-name">Kitchen/Pantry Makeover</h2>
    <p class="service-text">In-home customized nutrition workshop for individuals/families<br>focusing on health management and disease prevention<br>through food choices.</p>
    <h2 class="service-name">Farmers Market + Grocery Store Tour</h2>
    <p class="service-text">Grocery store or farmers market tours with full explanation of labels,<br>ingredients, and how to make the transition to a whole food lifestyle.</p>
    <h2 class="service-name">Cooking Classes</h2>
    <p class="service-text">Whole food, gluten, grain, sugar, dairy free + other dietary needs</p>
    <p class="service-text">Private or small group cooking classes at the retreat or at your location.<br>Learn to cook healthy and delicious meals for family and friends.</p>
    <p class="service-note">We offer individualized programming focused on overcoming health<br>challenges and chronic illness.</p>
    <p class="service-note">Customized on-site stays at the retreat will begin the pathway<br>to healing.</p>
  </div>

  <div class="panel bio-panel">
    <div class="bio-photo" role="img" aria-label="Photo of the founder running in a race"></div>
    <div class="bio-body">
      <h3 class="bio-name">MARLA QUINLAN MA, NC</h3>
      <ul class="bio-list">
        <li>Owner and founder of Sun Meadow Haven</li>
        <li>Certified nutrition educator</li>
        <li>Certified nutrition consultant</li>
        <li>NRCA certified running coach</li>
      </ul>
    </div>
  </div>

  <div class="contact-column">
    <div class="sunset-photo" role="img" aria-label="Photo of the desert sun setting behind a palm tree"></div>
    <div class="brand-strip">
      <span class="brand-name">Sun Meadow Haven</span>
      <span class="brand-dot"></span>
    </div>
    <div class="contact-block">
      <p class="contact-phone">555.014.2278</p>
      <p class="contact-line">sunmeadowhaven@mailbox.com</p>
      <p class="contact-line">www.sunmeadowhaven.net</p>
    </div>
  </div>
</section>

<section class="postcard postcard--visuals">
  <div class="photo pool-photo" role="img" aria-label="Photo of the retreat patio and pool beside a citrus tree"></div>

  <div class="panel offer-panel">
    <h1 class="offer-title">Sun Meadow Haven</h1>
    <ul class="offer-list">
      <li>Gluten Free Bed &amp; Breakfast</li>
      <li>Relaxing Wellness Retreat</li>
      <li>Whole Food &amp; Lifestyle Coaching</li>
      <li>Customized Nutrition Consulting</li>
    </ul>
  </div>

  <p class="motto-band">Small changes made consistently over time produce big results.</p>

  <div class="panel identity-panel">
    <div class="identity-mark">
      <span class="identity-dot"></span>
      <span class="identity-name">Sun Meadow Haven</span>
    </div>
    <div class="identity-divider"></div>
    <div class="identity-contact">
      <p class="identity-title">Sun Meadow Haven</p>
      <p class="identity-line">555.014.2278</p>
      <p class="identity-line">sunmeadowhaven@mailbox.com</p>
      <p class="identity-line">www.sunmeadowhaven.net</p>
      <p class="identity-line identity-city">Palm Mesa, CA</p>
    </div>
  </div>

  <div class="photo market-photo" role="img" aria-label="Photo of the founder holding fresh greens at a farmers market"></div>
</section>

</body>
</html>
```